Real Estate Investor needs awesome business card design

I invest in real estate, focused on multi-family properties, and I need a business card to hand out to potential partners. I prefer simple, clean designs, but it needs to stand out, so I'd like there to be a bit of red in the design as well.

It should include this information:

Front
Calder Whitby
Real Estate Investor
Direct phone: 501-555-0187
Email: calderjwhitby@mailbox-example.net
Headshot (Picture), I've uploaded a few, just pick the one you think looks best with your design. You can remove the background from the headshot image if it looks better.

Back
The back of the card's design should flow and be congruent with the front. On the back I want to put an inspirational quote or question. There will be different ones depending on the card, so I'll need the original file so I can edit it in the end.

For now, use “The Pessimist Sees Difficulty In Every Opportunity. The Optimist Sees The Opportunity In Every Difficulty.” -Edmund Halvorsen

Target Market(s)

Investors

Industry/Entity Type

Real Estate

Contact Information for Business Card

Front
Calder Whitby
Real Estate Investor

Back
The back of the card's design should flow and be congruent with the front. On the back I want to put an inspirational quote or question. There will be different ones depending on the card, so I'll need the original file so I can edit it in the end. I've uploaded some EXAMPLES of business cards with quotes on them. Don't copy but feel free to use them as inspiration.

The design will be printed on "ZAP sized" business cards
1039 x 697 pixels
with rounded corners

Font styles to use
Serif
Decorative
Script

Colors
ec1f27

Requirements
Must have
• Headshot, name, and other information in it.
• 1039 x 697 pixels
• Rounded corners
• Clean design that pops. I'm open to see any color background, including black.
• Headshots can be located here: https://www.filecrate-example.com/sh/8kx2vq71ld0pa3z/BQQTXL7mrrf9eT3Kq0HhgkLm2b?dl=0
Nice to have
• It would be awesome if the design included a personal signature or monogram, but if not I'll get a personal logo developed later and the card redesigned if I think it needs it.
Should not have
• Cluttered design

```html
<!DOCTYPE html>
<html lang="en">
<head>
<meta charset="utf-8">
<title>Calder Whitby — Business Card</title>
<link rel="stylesheet" href="https://fonts.googleapis.com/css2?family=Source+Sans+3:wght@400;600&family=Arvo:wght@400;700&display=swap">
<style>
  :root {
    --page-bg: #e6e6e6;
    --photo-dark: #141414;
    --photo-mid: #3a3a3a;
    --name-band: #222222;
    --card-white: #ffffff;
    --ink-grey: #444444;
    --back-navy: #272839;
    --text-light: #ffffff;
    --accent-red: #ec1f27;
    --card-radius: 14px;
  }
  * { margin: 0; padding: 0; box-sizing: border-box; }
  html, body {
    width: 1200px; height: 987px; overflow: hidden;
    background: var(--page-bg);
  }
  .card {
    position: absolute;
    top: 200px;
    width: 394px; height: 586px;
    overflow: hidden;
    border-radius: var(--card-radius);
  }
  .card-front { left: 191px; background: var(--card-white); }
  .card-back { left: 616px; background: var(--back-navy); }

  .headshot {
    position: absolute; left: 0; top: 0;
    width: 394px; height: 398px;
    background: radial-gradient(ellipse at 50% 40%, var(--photo-mid) 0%, var(--photo-dark) 75%);
  }
  .name-band {
    position: absolute; left: 0; top: 398px;
    width: 394px; height: 84px;
    background: var(--name-band);
    border-top: 4px solid var(--accent-red);
    color: var(--text-light);
    text-align: center;
    font-family: "Source Sans 3", sans-serif;
  }
  .name {
    margin-top: 13px;
    font-size: 27px; font-weight: 600;
    line-height: 30px; letter-spacing: 0.3px;
  }
  .role { font-size: 19px; font-weight: 400; line-height: 24px; }
  .contact {
    position: absolute; left: 0; top: 506px;
    width: 394px;
    text-align: center;
    font-family: "Source Sans 3", sans-serif;
    font-size: 19px; line-height: 25px;
    color: var(--ink-grey);
  }

  .quote {
    position: absolute; left: 100px; top: 56px;
    font-family: "Arvo", serif;
    font-size: 21px; line-height: 27.3px;
    color: var(--text-light);
    text-transform: uppercase;
  }
  .quote-mark {
    position: absolute;
    font-family: "Arvo", serif;
    font-weight: 700;
    font-size: 66px; line-height: 1;
    color: var(--accent-red);
  }
  .quote-open { left: 50px; top: 44px; }
  .quote-close { left: 241px; top: 248px; }
  .quote-author {
    position: absolute; left: 100px; top: 282px;
    font-family: "Arvo", serif;
    font-size: 10px; letter-spacing: 0.2px;
    color: var(--text-light);
    text-transform: uppercase;
  }
</style>
</head>
<body>
  <section class="card card-front">
    <div class="headshot" role="img" aria-label="Black and white headshot of Calder Whitby in a dark blazer"></div>
    <div class="name-band">
      <p class="name">CALDER WHITBY</p>
      <p class="role">Real Estate Investor</p>
    </div>
    <div class="contact">
      <p>calderjwhitby@mailbox-example.net</p>
      <p>501-555-0187</p>
    </div>
  </section>

  <section class="card card-back">
    <span class="quote-mark quote-open">“</span>
    <p class="quote">The pessimist sees<br>difficulty<br>in every<br>opportunity.<br>The optimist sees<br>the opportunity<br>in every<br>difficulty.</p>
    <span class="quote-mark quote-close">”</span>
    <p class="quote-author">Edmund Halvorsen</p>
  </section>
</body>
</html>
```